Carver Lindqvist Group Business Cards

We have a new logo, and want to design new business cards with it. We are 21 years in business, and want a fresh but professional look, so not a lot of extra stuff on the card. We are a recruiting and staffing firm focused on placing accounting and finance professionals in the Dallas TX area. I've attached our new logo that should be displayed on the cards. Here is what I think we want on the cards:
Ray Pemberly, CPA
Partner and Managing Director
8282 Orchard Vale Rd.
Suite 610
Dallas, TX 75391
O 214-555-0184
M 214-555-0237
ray@carverlindqvist.example
www.carverlindqvist.example

```html
<!DOCTYPE html>
<html lang="en">
<head>
<meta charset="utf-8">
<title>Carver Lindqvist Group – Business Card</title>
<link rel="stylesheet" href="https://fonts.googleapis.com/css2?family=Raleway:wght@300;400;500;600;700&display=swap">
<style>
  :root {
    --page-bg: #ffffff;
    --card-blue: #243c8f;
    --card-white: #ffffff;
    --brand-blue: #2b3fa0;
    --text-light: #f2f3f8;
    --text-muted: #b7c0e0;
    --rule-blue: #6f86d6;
    --shadow: rgba(0, 0, 0, 0.28);
  }
  html, body {
    margin: 0;
    padding: 0;
    width: 1200px;
    height: 1196px;
    overflow: hidden;
    background: var(--page-bg);
    font-family: "Raleway", sans-serif;
  }
  .card {
    position: absolute;
    left: 330px;
    top: 150px;
    width: 540px;
    height: 890px;
    background: var(--card-blue);
    box-shadow: 8px 10px 14px var(--shadow);
    overflow: hidden;
  }
  .card-header {
    position: absolute;
    left: 0;
    top: 0;
    width: 540px;
    height: 260px;
  }
  .brand-name {
    position: absolute;
    left: 0;
    top: 70px;
    width: 100%;
    text-align: center;
    color: var(--brand-blue);
    font-weight: 700;
    font-size: 34px;
    line-height: 1.15;
    letter-spacing: 1px;
    text-transform: uppercase;
  }
  .holder {
    position: absolute;
    left: 0;
    top: 318px;
    width: 100%;
    text-align: center;
  }
  .holder-name {
    color: var(--text-light);
    font-weight: 600;
    font-size: 33px;
    letter-spacing: 2px;
    text-transform: uppercase;
    margin: 0;
  }
  .holder-title {
    color: var(--text-muted);
    font-weight: 300;
    font-size: 17px;
    text-transform: uppercase;
    margin: 2px 0 0;
  }
  .holder-rule {
    width: 196px;
    height: 2px;
    background: var(--rule-blue);
    margin: 10px auto 0;
    border: 0;
  }
  .address {
    position: absolute;
    left: 0;
    top: 436px;
    width: 100%;
    text-align: center;
    color: var(--text-light);
    font-size: 22px;
    font-weight: 500;
    font-variant: small-caps;
    line-height: 1.45;
    font-style: normal;
  }
  .phones {
    position: absolute;
    left: 190px;
    top: 570px;
    color: var(--text-light);
    font-size: 22px;
    font-weight: 500;
    line-height: 1.45;
  }
  .online {
    position: absolute;
    left: 95px;
    top: 680px;
    color: var(--text-light);
    font-size: 16px;
    font-weight: 500;
    letter-spacing: 1px;
    text-transform: uppercase;
  }
  .online-row {
    display: flex;
    align-items: center;
    gap: 16px;
    height: 40px;
  }
  .online-row svg {
    width: 24px;
    height: 24px;
    flex: none;
  }
</style>
</head>
<body>
  <div class="card">
    <svg class="card-header" viewBox="0 0 540 260" aria-hidden="true">
      <path d="M0 0 H540 V245 Q300 280 0 195 Z" fill="var(--card-white)"/>
    </svg>
    <div class="brand-name">Carver Lindqvist<br>Group</div>

    <div class="holder">
      <h1 class="holder-name">Ray Pemberly, CPA</h1>
      <p class="holder-title">Partner and Managing Director</p>
      <hr class="holder-rule">
    </div>

    <address class="address">
      8282 Orchard Vale Rd.<br>
      Suite 610<br>
      Dallas, TX 75391
    </address>

    <div class="phones">
      O 214-555-0184<br>
      M 214-555-0237
    </div>

    <div class="online">
      <div class="online-row">
        <svg viewBox="0 0 24 24" fill="none" stroke="var(--text-light)" stroke-width="1.4">
          <path d="M3 10 L12 4 L21 10 V20 H3 Z"/>
          <path d="M3 10 L12 16 L21 10"/>
          <path d="M3 20 L10 14 M21 20 L14 14"/>
        </svg>
        <span>ray@carverlindqvist.example</span>
      </div>
      <div class="online-row">
        <svg viewBox="0 0 24 24" fill="none" stroke="var(--text-light)" stroke-width="1.4">
          <circle cx="12" cy="12" r="10"/>
          <ellipse cx="12" cy="12" rx="4.5" ry="10"/>
          <path d="M2 12 H22 M4 6.5 H20 M4 17.5 H20"/>
        </svg>
        <span>www.carverlindqvist.example</span>
      </div>
    </div>
  </div>
</body>
</html>
```